Design a large parking banner – mandatory ticket validation in the shop

Banner Size:
548 cm (width) x 154 cm (height)
Note: The banner will be placed in a metal frame at our parking lot entrance, fully visible to every incoming truck driver. The message must be easy to read from a distance.
Goal of the Banner:
To inform all truck drivers that they must validate their entry ticket inside the shop, even if they are parking for a short time.
The message must be displayed in multiple languages for international drivers.
Mandatory Content:
Main message – in multiple languages (clearly separated or stacked):
Dutch (NL): Vergeet je ticket niet te valideren in de shop – verplicht, ook bij kort parkeren!
French (FR): N'oubliez pas de valider votre ticket à la boutique – obligatoire, même pour un court arrêt !
English (EN): Don't forget to validate your entry ticket in the shop – mandatory, even for short stops!
German (DE): Vergessen Sie nicht, Ihr Einfahrticket im Shop zu entwerten – Pflicht, auch bei kurzem Parken!
Polish (PL): Nie zapomnij zatwierdzić biletu w sklepie – obowiązkowe, nawet przy krótkim postoju!
Romanian (RO): Nu uitați să validați biletul în magazin – obligatoriu, chiar și pentru opriri scurte!
You can include more languages if space allows, but these are essential.
Opening Hours Block (in one section below):
Shop Opening Hours
Mon – Fri: 05:30 – 22:00
Sat & Sun: 08:00 – 22:00
Style & Branding:
The design must match the visual identity of Haulpoint 41Ter
Please refer to the attached photos of existing parking signage for guidance on colors, typography, and layout style
Our logo (attached) must be clearly visible and professionally integrated
Feel free to use icons or pictograms to visually support the message (e.g., ticket, truck, arrow)
Readability is key – large, bold text and high contrast colors that are visible from a distance
Target Audience:
International truck drivers – people who need fast, clear communication. Not everyone speaks the local language, so visual clarity and multilingual messaging are critical.
File Requirements:
Print-ready file (PDF or EPS) – 300 dpi at 1:10 scale
Include 5 cm bleed on all sides
Provide open source files if possible (AI or PSD)

```html
<!DOCTYPE html>
<html lang="en">
<head>
<meta charset="utf-8">
<title>Haulpoint 41Ter – Ticket Validation Banner</title>
<link rel="stylesheet" href="https://fonts.googleapis.com/css2?family=Saira+Condensed:wght@500;600;700&display=swap">
<style>
  :root {
    --navy: #262a52;
    --red: #e52229;
    --blue: #1b84c6;
    --white: #ffffff;
    --page: #ffffff;
    --flag-nl-red: #e52229;
    --flag-blue: #21468b;
    --flag-black: #1a1a1a;
    --flag-gold: #f5c400;
  }
  * { box-sizing: border-box; margin: 0; padding: 0; }
  html, body {
    width: 1200px;
    height: 1184px;
    overflow: hidden;
    background: var(--page);
  }
  body {
    position: relative;
    font-family: "Saira Condensed", "Arial Narrow", sans-serif;
    color: var(--white);
  }
  .banner {
    position: absolute;
    left: 30px;
    top: 432px;
    width: 1140px;
    height: 320px;
    background: var(--navy);
    overflow: hidden;
  }
  .headline {
    position: absolute;
    left: 0; top: 0;
    width: 100%;
    height: 50px;
    display: flex;
    align-items: center;
    justify-content: center;
    font-weight: 600;
    font-size: 25px;
    letter-spacing: 0.1px;
    text-transform: uppercase;
  }
  .headline-rule {
    position: absolute;
    left: 0; top: 50px;
    width: 100%;
    height: 8px;
    background: var(--red);
  }
  .brand {
    position: absolute;
    left: 24px; top: 76px;
    width: 174px;
    display: flex;
    align-items: center;
    gap: 8px;
  }
  .brand-mark {
    width: 14px; height: 14px;
    background: var(--blue);
    flex: none;
  }
  .brand-name {
    font-weight: 700;
    font-size: 27px;
    line-height: 1;
    text-transform: uppercase;
    color: var(--white);
  }
  .direction-arrow {
    position: absolute;
    left: 32px; top: 166px;
    width: 162px; height: 48px;
  }
  .hours {
    position: absolute;
    left: 28px; top: 238px;
    width: 166px;
    text-align: center;
  }
  .hours-title {
    background: var(--red);
    font-weight: 600;
    font-size: 16px;
    line-height: 24px;
    text-transform: uppercase;
  }
  .hours-line {
    font-weight: 500;
    font-size: 15px;
    line-height: 22px;
    margin-top: 2px;
  }
  .hours-divider {
    height: 2px;
    background: var(--white);
    margin: 1px 2px;
  }
  .messages {
    position: absolute;
    left: 222px; top: 70px;
    right: 0;
    list-style: none;
  }
  .message {
    display: flex;
    height: 36px;
    margin-bottom: 14.5px;
  }
  .flag-box {
    width: 44px;
    height: 36px;
    background: var(--blue);
    padding: 3px;
    flex: none;
  }
  .flag-box svg {
    display: block;
    width: 100%;
    height: 100%;
    background: var(--white);
  }
  .message-text {
    flex: 1;
    margin-left: 5px;
    background: var(--blue);
    display: flex;
    align-items: center;
    padding-left: 21px;
    font-weight: 600;
    font-size: 19.5px;
    text-transform: uppercase;
    white-space: nowrap;
  }
</style>
</head>
<body>
  <section class="banner">
    <h1 class="headline">Don't forget to validate your entry ticket in the shop – mandatory, even for short stops!</h1>
    <div class="headline-rule"></div>

    <div class="brand">
      <span class="brand-mark"></span>
      <span class="brand-name">Haulpoint<br>41Ter</span>
    </div>

    <svg class="direction-arrow" viewBox="0 0 162 48" aria-label="Shop this way">
      <polygon points="0,24 68,0 68,12 162,11 162,35 68,36 68,48" fill="#ffffff"/>
    </svg>

    <div class="hours">
      <div class="hours-title">Shop opening hours</div>
      <div class="hours-line">MON - FRI : 05:30 - 22:00</div>
      <div class="hours-divider"></div>
      <div class="hours-line">SAT &amp; SUN : 08:00 - 22:00</div>
    </div>

    <ul class="messages">
      <li class="message" lang="nl">
        <span class="flag-box"><svg viewBox="0 0 38 30"><rect x="4" y="5" width="30" height="6" fill="var(--flag-nl-red)"/><rect x="4" y="19" width="30" height="6" fill="var(--flag-blue)"/></svg></span>
        <span class="message-text">Vergeet je ticket niet te valideren in de shop – verplicht, ook bij kort parkeren!</span>
      </li>
      <li class="message" lang="de">
        <span class="flag-box"><svg viewBox="0 0 38 30"><rect x="4" y="4" width="30" height="7" fill="var(--flag-black)"/><rect x="4" y="11" width="30" height="8" fill="var(--red)"/><rect x="4" y="19" width="30" height="7" fill="var(--flag-gold)"/></svg></span>
        <span class="message-text">Vergessen Sie nicht, Ihr Einfahrticket im Shop zu entwerten – Pflicht, auch bei kurzem Parken!</span>
      </li>
      <li class="message" lang="fr">
        <span class="flag-box"><svg viewBox="0 0 38 30"><rect x="4" y="5" width="30" height="6" fill="var(--flag-blue)"/><rect x="4" y="19" width="30" height="6" fill="var(--red)"/></svg></span>
        <span class="message-text">N'oubliez pas de valider votre ticket à la boutique – obligatoire, même pour un court arrêt !</span>
      </li>
      <li class="message" lang="pl">
        <span class="flag-box"><svg viewBox="0 0 38 30"><rect x="4" y="15" width="30" height="11" fill="var(--red)"/></svg></span>
        <span class="message-text">Nie zapomnij zatwierdzić biletu w sklepie – obowiązkowe, nawet przy krótkim postoju!</span>
      </li>
      <li class="message" lang="ro">
        <span class="flag-box"><svg viewBox="0 0 38 30"><rect x="4" y="4" width="30" height="7" fill="var(--flag-blue)"/><rect x="4" y="11" width="30" height="8" fill="var(--flag-gold)"/><rect x="4" y="19" width="30" height="7" fill="var(--red)"/></svg></span>
        <span class="message-text">Nu uitați să validați biletul în magazin – obligatoriu, chiar și pentru opriri scurte!</span>
      </li>
    </ul>
  </section>
</body>
</html>
```